brivel Card and stationary design
logo and stationary
Simple
Dennis Wallord
Agent/Advocate
4150 Harbor Ridge Lane
Suite 219
Greensboro, NC 27318
office- 336-592-8047
dennis@brivel7.com
www.brivel7.com
I will upload the logo to use for the card and stationary.
please use the file I upload for the content on the back.
Brivel new logo
card back content

```html
<!DOCTYPE html>
<html lang="en">
<head>
<meta charset="utf-8">
<title>Brivel Business Card</title>
<link rel="stylesheet" href="https://fonts.googleapis.com/css2?family=Arimo:wght@400;700&display=swap">
<style>
  :root {
    --purple: #5b2d8e;
    --purple-soft: #8a6fb3;
    --ink: #5b2d8e;
    --paper: #ffffff;
    --backdrop: #eeeae4;
    --rule: #d9d3e3;
  }
  * { margin: 0; padding: 0; box-sizing: border-box; }
  html, body {
    width: 1200px;
    height: 778px;
    overflow: hidden;
    background: var(--backdrop);
    font-family: "Arimo", Arial, sans-serif;
  }
  .card {
    position: absolute;
    left: 60px;
    top: 74px;
    width: 1080px;
    height: 630px;
    background: var(--paper);
    box-shadow: 0 4px 18px rgba(0,0,0,0.12);
    overflow: hidden;
  }
  .brand {
    position: absolute;
    left: 84px;
    top: 230px;
    display: flex;
    align-items: center;
    gap: 22px;
  }
  .brand-square {
    width: 56px;
    height: 56px;
    background: var(--purple);
  }
  .brand-name {
    font-size: 92px;
    font-weight: 400;
    color: var(--purple);
    line-height: 1;
  }
  .divider {
    position: absolute;
    left: 534px;
    top: 135px;
    width: 2px;
    height: 375px;
    background: var(--rule);
  }
  .contact {
    position: absolute;
    left: 598px;
    top: 140px;
    color: var(--ink);
  }
  .contact-name {
    font-size: 38px;
    font-weight: 700;
    line-height: 1.1;
  }
  .contact-role {
    font-size: 31px;
    margin-top: 6px;
  }
  .contact-address {
    margin-top: 48px;
    font-size: 26px;
    line-height: 42px;
  }
  .contact-lines {
    margin-top: 14px;
    font-size: 25px;
    line-height: 37px;
    list-style: none;
  }
  .contact-lines li {
    display: flex;
    align-items: center;
    gap: 12px;
  }
  .contact-lines svg {
    width: 18px;
    height: 18px;
    flex: none;
  }
  .band-rule {
    position: absolute;
    left: 0;
    top: 561px;
    width: 100%;
    height: 3px;
    background: var(--purple-soft);
  }
  .band {
    position: absolute;
    left: 0;
    top: 574px;
    width: 100%;
    height: 56px;
    background: var(--purple);
    display: flex;
    align-items: center;
    justify-content: center;
  }
  .band-url {
    color: #ffffff;
    font-size: 27px;
    font-weight: 700;
    letter-spacing: 6px;
  }
</style>
</head>
<body>
  <main class="card">
    <div class="brand">
      <span class="brand-square"></span>
      <span class="brand-name">Brivel</span>
    </div>

    <div class="divider"></div>

    <section class="contact">
      <h1 class="contact-name">Dennis Wallord</h1>
      <p class="contact-role">Agent/Advocate</p>
      <address class="contact-address" style="font-style:normal">
        4150 Harbor Ridge Lane<br>
        Suite 219<br>
        Greensboro, NC 27318
      </address>
      <ul class="contact-lines">
        <li>
          <svg viewBox="0 0 18 18" aria-hidden="true"><path d="M4 2c1 0 2 3 2 4s-1 1-1 2c1 2 3 4 5 5 1 0 1-1 2-1s4 1 4 2-2 3-3 3C7 17 1 11 1 5c0-1 2-3 3-3z" fill="var(--purple)"/></svg>
          office- 336-592-8047
        </li>
        <li>
          <svg viewBox="0 0 18 18" aria-hidden="true"><rect x="5" y="1" width="8" height="16" rx="1.5" fill="var(--purple)"/><rect x="6.5" y="3" width="5" height="9" fill="#fff"/></svg>
          336-715-4629
        </li>
        <li>
          <svg viewBox="0 0 18 18" aria-hidden="true"><rect x="1" y="4" width="16" height="11" fill="none" stroke="var(--purple)" stroke-width="1.6"/><path d="M1 4l8 6 8-6" fill="none" stroke="var(--purple)" stroke-width="1.6"/></svg>
          dennis@brivel7.com
        </li>
      </ul>
    </section>

    <div class="band-rule"></div>
    <footer class="band">
      <span class="band-url">www.brivel7.com</span>
    </footer>
  </main>
</body>
</html>
```